Bramble Creek Retreat Wedding and Event Venue

We are looking for a webpage for our Wedding and Event Venue just opened up in Eastern San Diego CA. It is out of a private home that has a very photogenic backyard including grapevines and orchard trees, a 15 ft waterfall into a pool and market lights hanging from trees, all connected by paved stone and compacted dirt paths

We are looking for something that will be very bright, warm and inviting to our clients. The clientele will be mostly couples between 22 and 35 years of age for the weddings and planners/executives age 22-60 for our corporate events.

We would like a rustic Outdoor look as that is what our venue showcases. You can see our facebook Here: https://www.facebook.com/BrambleCreekRetreat/

We would like for the pictures on the facebook to be used on the page. The google drive where most of them are located is here for full file sizes https://drive.example-share.com/open?id=7Q-9Kxw-M2pluT8RrWfLJd4XNV2

We would like to see designs that go with the colors of our logo and that included stone, wood, and grapevine textures as well as anything else rustic such as Market-lights.

The final design should be welcoming for newly engaged couples and corporations/companies who would like to book an outdoor venue for their wedding or next event. There can even be a simple first page with separate tabs for weddings and events that will be able to be more specially focused to the clients.

We would also like the option to be able to edit the pictures we place on the site seasonally as we would like our pictures to reflect our clients

Target Market(s)

Engaged couples age 22-35 and corporate planners/executives age 22-60

Industry/Entity Type

Events

Font styles to use
Script

Requirements
Must have
• Rustic Look, (wood, stone, wine vines/barrels, market lights, mason jars, etc)
• tab pages/sub pages for "About us", "Packages", "Pricing", "Gallery" (we must be able to put our pictures here from all our events), "What makes us Unique", "Contact us" that we are able to enter information into
Nice to have
• Colors matching our logo, Pictures from our Facebook page (listed in brief)
Should not have
• Corporate Look

```html
<!DOCTYPE html>
<html lang="en">
<head>
<meta charset="utf-8">
<title>Bramble Creek Retreat – Wedding and Event Venue</title>
<link href="https://fonts.googleapis.com/css2?family=Montserrat:wght@400;700&family=Philosopher:wght@400;700&family=Open+Sans:wght@400;600&display=swap" rel="stylesheet">
<style>
:root{
  --gold:#c3a24c;
  --gold-deep:#a9893a;
  --wood:#ebebe8;
  --wood-shade:#dededa;
  --ink:#2f2b24;
  --muted:#8d8a84;
  --dark:#3a3427;
  --green:#8ea688;
  --white:#ffffff;
}
*{box-sizing:border-box;margin:0;padding:0}
html,body{width:1200px;height:5070px;overflow:hidden}
body{position:relative;font-family:"Open Sans",sans-serif;color:var(--ink);background:var(--wood)}
.section{position:absolute;left:0;width:1200px}
.fill{position:absolute;inset:0}
.center{position:absolute;left:0;width:100%;text-align:center}
.heading{font-family:"Philosopher",sans-serif;font-size:34px;font-weight:400;color:var(--ink)}
.sub{font-size:14px;color:var(--gold);line-height:22px}
.body-text{font-size:14px;line-height:24px;color:var(--muted)}
.btn{position:absolute;left:50%;transform:translateX(-50%);height:44px;border-radius:22px;font-family:"Montserrat",sans-serif;font-size:12px;font-weight:700;letter-spacing:1px;display:flex;align-items:center;justify-content:center}

/* hero */
.hero{top:0;height:640px}
.hero-photo{background:linear-gradient(120deg,#4a4a32 0%,#6d6b4c 35%,#8c8a74 55%,#4f5238 80%,#3a3a28 100%)}
.hero-shade{background:rgba(20,18,12,.35)}
.brand{top:60px;font-family:"Philosopher",sans-serif;font-size:34px;color:var(--gold)}
.brand-mark{display:inline-block;width:14px;height:14px;border-radius:50%;background:var(--gold);margin-right:10px;vertical-align:middle}
.nav{position:absolute;top:186px;left:0;width:100%;display:flex;justify-content:center;gap:46px;font-family:"Montserrat",sans-serif;font-size:13px;font-weight:700;color:var(--white)}
.nav .active{color:var(--gold)}
.hero-title{top:280px;font-family:"Montserrat",sans-serif;font-size:56px;font-weight:700;color:var(--white);letter-spacing:1px}
.hero-tag{top:360px;font-family:"Philosopher",sans-serif;font-size:26px;color:var(--white)}
.hero .btn{top:422px;width:190px;border:2px solid var(--white);color:var(--white)}
.torn{position:absolute;left:0;width:1200px}

/* welcome */
.welcome{top:625px;height:660px;background:linear-gradient(90deg,var(--wood),#f2f2ef 40%,var(--wood-shade) 70%,var(--wood))}
.welcome-box{position:absolute;left:101px;top:152px;width:998px;height:413px;border:3px solid var(--gold)}
.welcome-box::after{content:"";position:absolute;inset:6px;border:1px solid var(--gold)}
.ornament{position:absolute;left:485px;top:115px;width:230px;height:56px;background:linear-gradient(90deg,#cbb26a,#b39646,#cbb26a);border-radius:28px;z-index:2}
.welcome .heading{top:232px}
.welcome .body-text{position:absolute;left:220px;top:288px;width:760px;text-align:center}
.welcome .btn{top:444px;width:150px;border:2px solid #bdbab2;color:#8d8a84}

/* photo band */
.band{top:1285px;height:500px}
.band-photo{background:linear-gradient(180deg,#3d4b2e 0%,#5c6a45 40%,#4a5a38 70%,#2e3a22 100%)}
.band-shade{background:rgba(15,15,10,.35)}
.band-text{top:190px;font-family:"Philosopher",sans-serif;font-size:38px;line-height:66px;color:var(--white)}

/* unique */
.unique{top:1785px;height:665px;background:linear-gradient(90deg,var(--wood-shade),#f2f2ef 50%,var(--wood))}
.unique .heading{top:80px}
.unique .sub{top:140px;left:330px;width:540px;color:var(--muted)}
.feature{position:absolute;top:278px;width:240px;text-align:center}
.feature-ring{width:155px;height:155px;margin:0 auto;border-radius:50%;border:3px solid var(--gold);display:flex;align-items:center;justify-content:center}
.feature-ring span{width:133px;height:133px;border-radius:50%;border:1px solid var(--gold);display:flex;align-items:center;justify-content:center}
.feature h3{margin-top:52px;font-family:"Philosopher",sans-serif;font-size:20px;font-weight:400}
.feature p{margin-top:12px;font-size:12px;line-height:19px;color:var(--muted)}

/* testimonial */
.testimonial{top:2450px;height:490px;background:linear-gradient(90deg,#c4a44c,#cdb060 50%,#c0a048)}
.quote-box{position:absolute;left:96px;top:68px;width:1008px;height:362px;border:2px solid rgba(255,255,255,.85)}
.quote-mark{top:100px;font-family:"Montserrat",sans-serif;font-size:120px;font-weight:700;line-height:120px;color:var(--white)}
.quote-text{position:absolute;left:230px;top:236px;width:740px;text-align:center;font-size:14px;line-height:24px;font-style:italic;color:var(--white)}
.quote-name{top:352px;font-family:"Montserrat",sans-serif;font-size:16px;font-weight:700;color:var(--white);letter-spacing:1px}

/* gallery */
.gallery{top:2940px;height:1010px;background:linear-gradient(180deg,#3f3829,var(--dark) 50%,#332d21)}
.gallery .heading{top:76px;color:var(--white)}
.gallery .sub{top:128px}
.grid{position:absolute;left:101px;top:224px;display:grid;grid-template-columns:repeat(4,230px);grid-auto-rows:216px;gap:24px 26px}
.tile{display:block}

/* partners */
.partners{top:3950px;height:875px;background:linear-gradient(90deg,var(--wood),#f2f2ef 50%,var(--wood-shade))}
.partners .heading{top:80px}
.partners .sub{top:130px}
.badge{position:absolute;width:170px;height:40px;background:#6b6b6b;border-radius:4px}

/* footer */
.footer{top:4825px;height:245px;background:var(--green);color:var(--white)}
.contact{position:absolute;top:45px;left:0;width:100%;display:flex;justify-content:center;gap:40px;font-size:13px;line-height:18px}
.contact-item{display:flex;align-items:center;gap:12px}
.icon-dot{width:32px;height:32px;border-radius:50%;border:1px solid rgba(255,255,255,.7);display:flex;align-items:center;justify-content:center}
.foot-nav{position:absolute;top:112px;left:0;width:100%;display:flex;justify-content:center;gap:14px;font-family:"Montserrat",sans-serif;font-size:12px;font-weight:700}
.rule{position:absolute;left:0;top:158px;width:100%;height:1px;background:rgba(255,255,255,.45)}
.copyright{position:absolute;left:100px;top:188px;font-size:11px}
.socials{position:absolute;right:100px;top:178px;display:flex;gap:10px}
.socials span{width:30px;height:30px;border-radius:50%;background:rgba(255,255,255,.85)}
</style>
</head>
<body>

<header class="section hero">
  <div class="fill hero-photo" role="img" aria-label="Couple embracing on a garden terrace at the venue"></div>
  <div class="fill hero-shade"></div>
  <div class="center brand"><span class="brand-mark"></span>Bramble Creek Retreat</div>
  <nav class="nav">
    <span class="active">HOME</span><span>ABOUT US</span><span>PACKAGES</span><span>PRICING</span><span>GALLERY</span><span>WHAT MAKES US UNIQUE</span><span>CONTACT US</span>
  </nav>
  <h1 class="center hero-title">BRAMBLE CREEK RETREAT</h1>
  <p class="center hero-tag">We are a Wedding and Event Venue</p>
  <div class="btn">BOOK YOUR EVENT</div>
  <svg class="torn" style="bottom:0" width="1200" height="40" viewBox="0 0 1200 40" aria-hidden="true">
    <path d="M0 22 L40 14 L80 24 L120 12 L170 26 L220 16 L260 28 L310 14 L360 22 L410 10 L460 24 L510 16 L560 28 L610 12 L660 22 L710 14 L760 26 L810 12 L860 24 L910 16 L960 28 L1010 14 L1060 22 L1110 12 L1160 24 L1200 16 L1200 40 L0 40Z" fill="#ebebe8"/>
  </svg>
</header>

<section class="section welcome">
  <div class="ornament" role="img" aria-label="Gold scroll ornament"></div>
  <div class="welcome-box"></div>
  <h2 class="center heading">Welcome to Bramble Creek Retreat</h2>
  <p class="body-text">Set among orchard rows and old grapevines, our family home opens its gardens for weddings, showers and company gatherings. Guests wander stone paths under market lights, pause by the waterfall pool and linger long after the last toast. We keep every day personal, relaxed and entirely yours.</p>
  <div class="btn">ABOUT US</div>
</section>

<section class="section band">
  <div class="fill band-photo" role="img" aria-label="Guests gathered in the backyard garden under trees and umbrellas"></div>
  <div class="fill band-shade"></div>
  <p class="center band-text">We are a private home that has a very photogenic<br>backyard including grapevines &amp; orchard trees</p>
</section>

<section class="section unique">
  <h2 class="center heading">What makes us Unique</h2>
  <p class="center sub">A quiet hillside setting with room to celebrate, flexible dates and a team that has hosted gatherings of every size and style.</p>

  <div class="feature" style="left:90px">
    <div class="feature-ring"><span>
      <svg width="56" height="56" viewBox="0 0 24 24" aria-hidden="true"><path d="M12 2l3 6.5 7 .8-5.2 4.8 1.4 7L12 17.6 5.8 21.1l1.4-7L2 9.3l7-.8z" fill="none" stroke="#c3a24c" stroke-width="1.6" stroke-linejoin="round"/></svg>
    </span></div>
    <h3>Exciting Exhibit</h3>
    <p>Gardens, vines and a waterfall<br>pool to explore.</p>
  </div>
  <div class="feature" style="left:346px">
    <div class="feature-ring"><span>
      <svg width="56" height="56" viewBox="0 0 24 24" aria-hidden="true"><rect x="3" y="5" width="18" height="16" rx="1.5" fill="none" stroke="#c3a24c" stroke-width="1.6"/><path d="M3 10h18M8 3v4M16 3v4M7 13h2M11 13h2M15 13h2M7 17h2M11 17h2M15 17h2" stroke="#c3a24c" stroke-width="1.6"/></svg>
    </span></div>
    <h3>Flexible Booking</h3>
    <p>Choose weekday or weekend<br>dates that suit you.</p>
  </div>
  <div class="feature" style="left:610px">
    <div class="feature-ring"><span>
      <svg width="60" height="60" viewBox="0 0 24 24" aria-hidden="true"><path d="M1.5 12S5.5 5 12 5s10.5 7 10.5 7-4 7-10.5 7S1.5 12 1.5 12z" fill="#c3a24c"/><circle cx="12" cy="12" r="4" fill="#ebebe8"/><circle cx="12" cy="12" r="2" fill="#c3a24c"/></svg>
    </span></div>
    <h3>Stunning Views</h3>
    <p>Sunset views across orchards<br>and rolling hills.</p>
  </div>
  <div class="feature" style="left:870px">
    <div class="feature-ring"><span>
      <svg width="60" height="60" viewBox="0 0 24 24" aria-hidden="true"><circle cx="12" cy="8" r="3.2" fill="#c3a24c"/><circle cx="5.5" cy="9.5" r="2.4" fill="#c3a24c"/><circle cx="18.5" cy="9.5" r="2.4" fill="#c3a24c"/><path d="M6 19c0-3.5 2.7-6 6-6s6 2.5 6 6z" fill="#c3a24c"/><path d="M1 18c0-2.6 2-4.5 4.5-4.5 1 0 1.8.3 2.5.8-1.3 1-2.2 2.3-2.5 3.7zM23 18c0-2.6-2-4.5-4.5-4.5-1 0-1.8.3-2.5.8 1.3 1 2.2 2.3 2.5 3.7z" fill="#c3a24c"/></svg>
    </span></div>
    <h3>National Expertise</h3>
    <p>Planners who know every<br>corner of the grounds.</p>
  </div>
</section>

<section class="section testimonial">
  <div class="quote-box"></div>
  <div class="center quote-mark">&ldquo;</div>
  <p class="quote-text">&ldquo;Our day felt like a garden party with our closest friends. The lights came on over the vines just as the toasts began, and every photo looks like a painting. The team handled each detail so we could simply enjoy it.&rdquo;</p>
  <p class="center quote-name">ELLA &amp; MARCUS</p>
</section>

<section class="section gallery">
  <h2 class="center heading">Gallery</h2>
  <p class="center sub">Moments captured across our gardens and grounds</p>
  <div class="grid">
    <div class="tile" role="img" aria-label="Lounge seating on the lawn" style="background:linear-gradient(135deg,#5a6a3c,#b8a98a)"></div>
    <div class="tile" role="img" aria-label="White ceremony chairs in rows" style="background:linear-gradient(135deg,#7c8a58,#e2e0d6)"></div>
    <div class="tile" role="img" aria-label="Guests seated at reception tables" style="background:linear-gradient(135deg,#8a8470,#d2cbbd)"></div>
    <div class="tile" role="img" aria-label="Guests playing lawn games" style="background:linear-gradient(135deg,#4d6a3a,#8fa06a)"></div>
    <div class="tile" role="img" aria-label="Friends relaxing by the pool" style="background:linear-gradient(135deg,#3f5a4a,#9aa89a)"></div>
    <div class="tile" role="img" aria-label="Couple at the sweetheart table" style="background:linear-gradient(135deg,#4a4636,#a49a84)"></div>
    <div class="tile" role="img" aria-label="Tiered wedding cake on a dessert table" style="background:linear-gradient(135deg,#cfc7b8,#f2efe8)"></div>
    <div class="tile" role="img" aria-label="Table setting with name cards" style="background:linear-gradient(135deg,#b2443e,#e8e2d8)"></div>
    <div class="tile" role="img" aria-label="Mason jar centerpiece with table card" style="background:linear-gradient(135deg,#d8d4cc,#8e8a80)"></div>
    <div class="tile" role="img" aria-label="Guests mingling in the garden" style="background:linear-gradient(135deg,#4c5a36,#9a8e74)"></div>
    <div class="tile" role="img" aria-label="Couple posing among the trees" style="background:linear-gradient(135deg,#5c5544,#c8bfae)"></div>
    <div class="tile" role="img" aria-label="Reception under the orchard canopy" style="background:linear-gradient(135deg,#3e5a2e,#a4b07c)"></div>
  </div>
</section>

<section class="section partners">
  <h2 class="center heading">Our Partners</h2>
  <p class="center sub">Friends who help make every event shine</p>
  <div class="badge" style="left:185px;top:248px"></div>
  <div class="badge" style="left:557px;top:248px"></div>
  <div class="badge" style="left:878px;top:248px"></div>
  <div class="badge" style="left:185px;top:367px"></div>
  <div class="badge" style="left:557px;top:367px"></div>
  <div class="badge" style="left:878px;top:367px"></div>
  <div class="badge" style="left:185px;top:502px"></div>
  <div class="badge" style="left:557px;top:502px"></div>
  <div class="badge" style="left:878px;top:502px"></div>
  <div class="badge" style="left:185px;top:627px"></div>
  <div class="badge" style="left:557px;top:627px"></div>
  <div class="badge" style="left:878px;top:627px"></div>
</section>

<footer class="section footer">
  <svg class="torn" style="top:-30px" width="1200" height="34" viewBox="0 0 1200 34" aria-hidden="true">
    <path d="M0 18 L50 10 L100 20 L150 8 L200 22 L250 12 L300 24 L350 10 L400 20 L450 8 L500 22 L550 12 L600 24 L650 10 L700 20 L750 8 L800 22 L850 12 L900 24 L950 10 L1000 20 L1050 8 L1100 22 L1150 12 L1200 20 L1200 34 L0 34Z" fill="#8ea688"/>
  </svg>
  <div class="contact">
    <div class="contact-item">
      <span class="icon-dot"><svg width="14" height="14" viewBox="0 0 24 24" aria-hidden="true"><path d="M12 2a7 7 0 0 0-7 7c0 5 7 13 7 13s7-8 7-13a7 7 0 0 0-7-7zm0 9.5a2.5 2.5 0 1 1 0-5 2.5 2.5 0 0 1 0 5z" fill="#fff"/></svg></span>
      <span>214 Orchard Lane, Suite 3<br>Alpine, CA 91901</span>
    </div>
    <div class="contact-item">
      <span class="icon-dot"><svg width="14" height="14" viewBox="0 0 24 24" aria-hidden="true"><path d="M6.6 10.8a15 15 0 0 0 6.6 6.6l2.2-2.2c.3-.3.7-.4 1-.2 1.1.4 2.3.6 3.6.6.6 0 1 .4 1 1V20c0 .6-.4 1-1 1A17 17 0 0 1 3 4c0-.6.4-1 1-1h3.5c.6 0 1 .4 1 1 0 1.3.2 2.5.6 3.6.1.3 0 .7-.2 1z" fill="#fff"/></svg></span>
      <span>+1 555 014 2290</span>
    </div>
    <div class="contact-item">
      <span class="icon-dot"><svg width="14" height="14" viewBox="0 0 24 24" aria-hidden="true"><path d="M3 5h18v14H3z" fill="none" stroke="#fff" stroke-width="2"/><path d="M3 5l9 8 9-8" fill="none" stroke="#fff" stroke-width="2"/></svg></span>
      <span>info@bramblecreekretreat.com</span>
    </div>
  </div>
  <nav class="foot-nav">
    <span>HOME</span><span>|</span><span>ABOUT US</span><span>|</span><span>PACKAGES</span><span>|</span><span>PRICING</span><span>|</span><span>GALLERY</span><span>|</span><span>WHAT MAKES US UNIQUE</span><span>|</span><span>CONTACT US</span>
  </nav>
  <div class="rule"></div>
  <p class="copyright">Copyright © 2017, Bramble Creek Retreat. All rights reserved. Legal Disclaimer</p>
  <div class="socials"><span></span><span></span><span></span><span></span></div>
</footer>

</body>
</html>
```